Lantern Business Cards

Need business cards for my employees at my restaurant.

Needs to include:
Our Logo
Lantern Bowls & Brews
Name: Nora Pettigrew
Title : Owner
Address: 487 Mirella Ave. Lake Havasu City, AZ 86519
Web: www.lanternkestrel.com
Phone: 928-555-0147
Cell: 928-555-0192
Email: info@lanternkestrel.com

```html
<!DOCTYPE html>
<html lang="en">
<head>
<meta charset="utf-8">
<title>Lantern Bowls &amp; Brews — Business Card</title>
<link rel="stylesheet" href="https://fonts.googleapis.com/css2?family=Exo+2:wght@600;800&family=Roboto:wght@400;700&display=swap">
<style>
  :root {
    --stage: #2a2a2a;
    --card-white: #ffffff;
    --brand-red: #c8202f;
    --deep-red: #8e1318;
    --ink: #1b1b1b;
    --muted: #555555;
  }
  * { box-sizing: border-box; margin: 0; padding: 0; }
  html, body { width: 1200px; height: 800px; overflow: hidden; }
  body {
    background: var(--stage);
    font-family: "Roboto", Arial, sans-serif;
    position: relative;
  }
  .card {
    position: absolute;
    left: 320px;
    width: 560px;
    height: 320px;
    border-radius: 16px;
    overflow: hidden;
  }
  .card--front { top: 50px; background: var(--card-white); }
  .card--back { top: 430px; }

  .front__brand {
    position: absolute; left: 0; top: 0; width: 270px; height: 100%;
    display: flex; align-items: center; justify-content: center; gap: 10px;
  }
  .brand-mark { width: 22px; height: 22px; background: var(--brand-red); }
  .brand-name {
    font-family: "Exo 2", sans-serif; font-weight: 800;
    font-size: 40px; letter-spacing: 1px; color: var(--brand-red);
  }
  .front__divider {
    position: absolute; left: 276px; top: 70px; width: 1.5px; height: 180px;
    background: var(--brand-red);
  }
  .front__details { position: absolute; left: 300px; top: 62px; }
  .person-name {
    font-family: "Exo 2", sans-serif; font-weight: 800;
    font-size: 26px; color: var(--brand-red); letter-spacing: .5px;
  }
  .person-title { font-weight: 700; font-size: 13px; color: var(--ink); margin-top: 2px; }
  .address { font-size: 13px; color: var(--muted); line-height: 1.3; margin-top: 10px; }
  .contact-list { list-style: none; margin-top: 10px; }
  .contact-list li {
    display: flex; align-items: center; gap: 10px;
    font-size: 13px; color: var(--ink); line-height: 1.7;
  }
  .contact-list svg { width: 12px; height: 12px; flex: none; }
  .front__band { position: absolute; left: 0; bottom: 0; width: 100%; height: 12px; }

  .back__texture {
    position: absolute; inset: 0;
    background: radial-gradient(ellipse at 75% 25%, #d9332c 0%, var(--brand-red) 35%, var(--deep-red) 100%);
  }
  .back__brand {
    position: absolute; inset: 0;
    display: flex; align-items: center; justify-content: center; gap: 12px;
  }
  .back__brand .brand-mark { background: #ffffff; width: 26px; height: 26px; }
  .back__brand .brand-name { color: #ffffff; font-size: 50px; }
</style>
</head>
<body>
  <section class="card card--front" aria-label="Business card front">
    <div class="front__brand">
      <span class="brand-mark"></span>
      <span class="brand-name">LANTERN</span>
    </div>
    <div class="front__divider"></div>
    <div class="front__details">
      <h1 class="person-name">NORA PETTIGREW</h1>
      <p class="person-title">Owner</p>
      <p class="address">487 Mirella Ave. Lake<br>Havasu City, AZ 86519</p>
      <ul class="contact-list">
        <li><svg viewBox="0 0 12 12"><circle cx="6" cy="6" r="6" fill="var(--brand-red)"/><path d="M4 3.5l1 1.2-.6.8a3.5 3.5 0 0 0 2 2l.8-.6 1.2 1-.8.9C5.5 8.5 3.5 6.5 3.2 4.3z" fill="#fff"/></svg>928-555-0192</li>
        <li><svg viewBox="0 0 12 12"><circle cx="6" cy="6" r="6" fill="var(--brand-red)"/><rect x="3" y="5" width="6" height="3.5" rx="1" fill="#fff"/><rect x="4" y="3.5" width="4" height="1.2" rx=".5" fill="#fff"/></svg>928-555-0147</li>
        <li><svg viewBox="0 0 12 12"><path d="M1 6.5L11 1 7.5 11 6 7z" fill="var(--brand-red)"/></svg>info@lanternkestrel.com</li>
        <li><svg viewBox="0 0 12 12"><circle cx="6" cy="6" r="6" fill="var(--brand-red)"/><path d="M1 6h10M6 1c-2.5 3-2.5 7 0 10M6 1c2.5 3 2.5 7 0 10" stroke="#fff" stroke-width=".8" fill="none"/></svg>www.lanternkestrel.com</li>
      </ul>
    </div>
    <svg class="front__band" viewBox="0 0 560 12" preserveAspectRatio="none">
      <polygon points="0,12 300,12 310,0 0,0" fill="#ffffff"/>
      <polygon points="300,12 310,0 316,0 306,12" fill="var(--ink)"/>
      <polygon points="306,12 316,0 560,0 560,12" fill="var(--brand-red)"/>
    </svg>
  </section>

  <section class="card card--back" aria-label="Business card back">
    <div class="back__texture" role="img" aria-label="Red sparkling glitter texture"></div>
    <div class="back__brand">
      <span class="brand-mark"></span>
      <span class="brand-name">LANTERN</span>
    </div>
  </section>
</body>
</html>
```